依頼詳細
■コンペで依頼するもの
・トップページ(ワイヤーフレーム参照)
■当選後に依頼するもの
・第2階層ページ(ワイヤーフレーム参照)
・記事ページ(ワイヤーフレーム参照)
・アイキャッチ画像6種類

当選後、追加依頼をプロジェクト形式で発注しますので、受注できる方でお願いします。
追加依頼の予算は4万円以内です。
サイトURL
http://www.morinoyashiro-sample.jp/wp/
ページ数
1ページ
希望イメージ
シンプル 複雑
単色 カラフル
暗い 明るい
日常 高級
遊び心 厳粛
未来的 伝統的
女性的 男性的
希望する色
背景は白指定です。他はお任せします。
納品ファイル
• フォトショップ形式 (.psd)
• PNG形式 (.png)
補足説明
■参考サイト
http://kotobukisha-example.or.jp/jingu/
http://www.hanazakura-example.or.jp/top.php
http://fukuo-mitama.or.jp/

■素材
添付のワイヤーフレームと写真です。
写真は次のアドレスからダウンロードしてください。
http://pelotix.net/morinoyashiro/sozai.zip
現行サイトの画像も利用して頂いて構いません。

※メニュー部の配置は自由にして頂いて構いません。
※ボックス内の文字は画像データとして利用します。他の文字はテキストデータで利用します。
※他有料素材も5千円程度まではお支払できます。

神紋(ロゴマーク)の色は自由に設定して頂いて構いません。
深緑以外であれば問題ないようです。
現行サイトのロゴには「北原郷総鎮守」が含まれています。
ですが、今回はトップページから削除することが決定しています。
説明が不足しておりまして申し訳ございません。
ワイヤーフレーム内、サイトマップのテキストは確定していません。
デザインが分かれば大丈夫です。ダミーのテキストを入れてください。
レスポンシブ対応とありますが、対応は当方で行います。
今回、PC版トップページのイメージアップが最優先ですので、
コンペではレスポンシブを意識せずにデザインして頂いて構いません。
よろしくお願いします。
23日(月) 14:00より選考を開始します。
一時停止の理由:たくさんのご提案を頂きましてありがとうございました。
現在クライアントを含めた席で協議中ですが、どれもクオリティが高く難航しています。
本日中には決定する見込みです。

全体の配色、写真の扱い方を考慮した結果、「クライアントのイメージに近い」という事で選択させて頂きました。

沢山のご提案、誠にありがとうございました。

```html
<!DOCTYPE html>
<html lang="ja">
<head>
<meta charset="utf-8">
<title>杜乃宮</title>
<link rel="stylesheet" href="https://fonts.googleapis.com/css2?family=Noto+Serif+JP:wght@400;700&family=Noto+Sans+JP:wght@400;700&display=swap">
<style>
:root{
  --ink:#2b2624;
  --ink-soft:#3d3633;
  --gold:#b9a16a;
  --gold-dark:#9c8452;
  --red:#a5291f;
  --paper:#ffffff;
  --line:#d9d4cc;
  --grey:#8a8580;
  --pale:#f1eee9;
  --text:#3a3532;
}
*{box-sizing:border-box;margin:0;padding:0}
html,body{width:769px;height:1200px;overflow:hidden}
body{background:var(--paper);font-family:"Noto Sans JP",sans-serif;color:var(--text);font-size:7px;line-height:1.5;position:relative}
.serif{font-family:"Noto Serif JP",serif}

.topline{height:12px;background:var(--ink);color:#bdb5aa;font-size:5.5px;padding:2px 16px;line-height:8px}
.hero{position:relative;height:265px;background:linear-gradient(180deg,#3e5a3a 0%,#6d3a2a 45%,#8c2f22 70%,#4a3a2c 100%)}
.hero-logo{position:absolute;left:18px;top:16px;display:flex;align-items:center;gap:8px;color:#fff;font-family:"Noto Serif JP",serif;font-weight:700;font-size:22px;letter-spacing:3px}
.hero-logo .mark{width:26px;height:26px;border-radius:50%;background:#fff}
.hero-links{position:absolute;right:18px;top:16px;display:flex;gap:3px}
.hero-links span{display:block;width:48px;height:13px;background:rgba(43,38,36,.85);color:#ddd;font-size:5.5px;text-align:center;line-height:13px}
.hero-links span:first-child{background:var(--gold);color:#fff}
.hero-word{position:absolute;right:86px;top:86px;color:#fff;font-family:"Noto Serif JP",serif;text-align:center}
.hero-word b{display:block;font-size:40px;font-weight:400;line-height:1}
.hero-word small{font-size:8px;letter-spacing:3px}

.gnav{position:absolute;left:97px;top:277px;width:575px;height:35px;background:#fff;display:flex;box-shadow:0 1px 3px rgba(0,0,0,.15)}
.gnav a{flex:1;text-align:center;line-height:35px;font-family:"Noto Serif JP",serif;font-size:8px;color:var(--text);text-decoration:none;border-right:1px solid var(--line)}
.gnav a.current{background:var(--gold);color:#fff;flex:1.3}
.gnav a:last-child{border:0}

.wrap{position:absolute;left:97px;top:328px;width:575px;display:flex;gap:12px}
.main{width:430px}
.side{width:133px}

.feature{display:flex;height:146px}
.feature-label{width:133px;background:var(--ink);color:#fff;text-align:center;font-family:"Noto Serif JP",serif;padding-top:18px}
.feature-label .tag{font-size:5.5px;color:#cfc6b8}
.feature-label .kanji{font-size:38px;line-height:1.2;margin-top:6px;border-top:1px solid #6b625c;border-bottom:1px solid #6b625c;margin:8px 22px 0}
.feature-label .yomi{font-size:7px;letter-spacing:3px;margin-top:4px}
.feature-photo{flex:1;background:linear-gradient(135deg,#e9e5dc,#b8b2a8 55%,#5d5650)}

.news{margin-top:16px;position:relative;height:62px}
.news h2{font-family:"Noto Serif JP",serif;font-size:13px;font-weight:400;color:var(--ink)}
.news h2 small{font-size:6px;color:var(--grey);margin-left:4px}
.news ul{list-style:none;position:absolute;left:210px;top:2px;font-size:5.8px;color:var(--text)}
.news li{line-height:10px}
.news .more{position:absolute;right:0;bottom:2px}
.btn{display:inline-block;background:var(--ink);color:#fff;font-size:6px;padding:0 10px;height:13px;line-height:13px}

.cards{margin-top:12px;display:grid;grid-template-columns:repeat(3,1fr);gap:14px 12px}
.card h3{font-family:"Noto Serif JP",serif;font-weight:400;font-size:7.5px;border-bottom:1px solid var(--line);padding:0 0 3px 4px;border-left:2px solid var(--red);line-height:10px}
.card .ph{height:80px;margin-top:5px}
.card p{font-size:5.5px;line-height:8.5px;margin-top:5px;color:var(--text)}
.card .link{display:block;text-align:right;font-size:5.5px;color:var(--grey);margin-top:3px}
.ph1{background:linear-gradient(150deg,#6f8a5f,#3d4f35)}
.ph2{background:linear-gradient(150deg,#c9b9a0,#7a6b5a)}
.ph3{background:linear-gradient(150deg,#d8cfc2,#8d5a48)}
.ph4{background:linear-gradient(150deg,#7d9870,#55674a)}
.ph5{background:linear-gradient(150deg,#d7d2c8,#9a8c7a)}
.ph6{background:linear-gradient(150deg,#b6c6d2,#a5433a)}

.sched-head{background:var(--ink);color:#fff;font-family:"Noto Serif JP",serif;font-size:9px;padding:0 8px;height:26px;line-height:26px}
.sched-head small{font-size:5.5px;color:#cfc6b8;margin-left:4px}
.sched{list-style:none;background:var(--pale)}
.sched li{padding:6px 8px;border-bottom:1px solid #fff;height:38px}
.sched .date{display:inline-block;background:#9b958e;color:#fff;font-size:5.5px;padding:0 5px;line-height:9px}
.sched .title{display:block;color:var(--red);font-size:6px;margin-top:4px}
.sched-btn{display:block;text-align:center;margin-top:6px;background:var(--ink);color:#fff;font-size:6px;height:16px;line-height:16px}
.banners{margin-top:20px;display:flex;flex-direction:column;gap:8px}
.banner{height:56px;position:relative;background:linear-gradient(135deg,#aab9c4,#56687a)}
.banner:nth-child(2){background:linear-gradient(135deg,#c8b69a,#6e5b48)}
.banner:nth-child(3){background:linear-gradient(135deg,#9fb08f,#4d5d44)}
.banner:nth-child(4){background:linear-gradient(135deg,#c0c6cf,#7c6c66)}
.banner span{position:absolute;right:6px;bottom:6px;background:var(--red);color:#fff;font-family:"Noto Serif JP",serif;font-size:6px;padding:2px 5px}

.footer{position:absolute;left:0;top:973px;width:769px;height:205px;background:var(--ink);color:#d5cdc2}
.footer .pagetop{position:absolute;right:97px;top:-14px;background:var(--ink-soft);color:#fff;font-size:5.5px;height:14px;line-height:14px;padding:0 10px}
.f-brand{position:absolute;left:97px;top:30px}
.f-brand .name{display:flex;align-items:center;gap:7px;color:#fff;font-family:"Noto Serif JP",serif;font-weight:700;font-size:18px;letter-spacing:3px}
.f-brand .mark{width:22px;height:22px;border-radius:50%;background:#fff}
.f-brand p{font-size:5.5px;line-height:9px;margin-top:14px}
.f-map{position:absolute;left:330px;top:28px;display:flex;gap:26px}
.f-map h4{font-family:"Noto Serif JP",serif;font-weight:400;font-size:7.5px;color:#fff;border-bottom:1px solid #5a524d;padding-bottom:3px;margin-bottom:6px;width:100px}
.f-map ul{list-style:none;font-size:5.5px;line-height:10px}
.f-map .two{display:flex;gap:14px}
.f-map .two ul{width:60px}
.copy{position:absolute;left:0;top:1178px;width:769px;height:22px;background:var(--red);color:#f3d9d4;font-size:5.5px;text-align:right;padding-right:97px;line-height:22px}
</style>
</head>
<body>

<div class="topline">北原郷総鎮守　杜乃宮 公式サイト ― 森と社の祈りを伝える</div>

<header class="hero" role="img" aria-label="朱塗りの楼門と杉木立の写真">
  <div class="hero-logo"><span class="mark"></span>杜乃宮</div>
  <div class="hero-links"><span>参拝案内</span><span>交通案内</span><span>お問合せ</span><span>English</span></div>
  <div class="hero-word"><b>祷</b><small>いのる</small></div>
</header>

<nav class="gnav">
  <a class="current" href="#">杜乃宮について</a>
  <a href="#">祭典・行事</a>
  <a href="#">参拝・その他祭典</a>
  <a href="#">境内・周辺案内</a>
  <a href="#">御守・御札</a>
  <a href="#">特集</a>
</nav>

<div class="wrap">
  <main class="main">
    <section class="feature">
      <div class="feature-label">
        <div class="tag">例大祭特集</div>
        <div class="kanji">祀</div>
        <div class="yomi">まつる</div>
      </div>
      <div class="feature-photo" role="img" aria-label="白装束の神職が列をなして進む祭礼行列の写真"></div>
    </section>

    <section class="news">
      <h2>最新情報<small>NEWS</small></h2>
      <ul>
        <li>平成28年5月1日　春季例大祭の斎行について</li>
        <li>平成28年4月20日　御朱印・授与品のご案内</li>
        <li>平成28年4月2日　境内整備に伴う参道通行止め</li>
      </ul>
      <span class="btn more">最新情報一覧</span>
    </section>

    <section class="cards">
      <article class="card"><h3>杜乃宮について</h3><div class="ph ph1" role="img" aria-label="杉木立の中の社殿の写真"></div><p>古くより北原郷を守る社として崇敬を集め、豊かな森に抱かれた境内には今も静かな祈りの時が流れています。</p><span class="link">詳しく見る</span></article>
      <article class="card"><h3>祭事・行事</h3><div class="ph ph2" role="img" aria-label="拝殿での神事の写真"></div><p>年間を通じて数多くの祭典が斎行されます。季節ごとの行事と神事の由来を分かりやすくご紹介いたします。</p><span class="link">詳しく見る</span></article>
      <article class="card"><h3>参拝・その他祭典</h3><div class="ph ph3" role="img" aria-label="参拝者が集う境内の写真"></div><p>初宮詣や七五三、厄除けなどのご祈祷を承っております。受付時間や初穂料についてはこちらをご覧ください。</p><span class="link">詳しく見る</span></article>
      <article class="card"><h3>境内・周辺案内</h3><div class="ph ph4" role="img" aria-label="緑に囲まれた参道の写真"></div><p>境内に点在する摂末社や御神木、周辺の名所まで、散策の目安となる案内と地図をご用意しました。</p><span class="link">詳しく見る</span></article>
      <article class="card"><h3>御守・御札</h3><div class="ph ph5" role="img" aria-label="授与所の建物の写真"></div><p>交通安全や家内安全、学業成就など、様々な願いに応じた御守・御札を授与所にてお頒ちしております。</p><span class="link">詳しく見る</span></article>
      <article class="card"><h3>特集</h3><div class="ph ph6" role="img" aria-label="湖上を進む御船祭の写真"></div><p>十二年に一度斎行される御船祭をはじめ、杜乃宮に伝わる特別な祭礼と歴史を特集でお届けします。</p><span class="link">詳しく見る</span></article>
    </section>
  </main>

  <aside class="side">
    <div class="sched-head">行事予定<small>SCHEDULE</small></div>
    <ul class="sched">
      <li><span class="date">平成28年5月1日</span><span class="title">春季例大祭</span></li>
      <li><span class="date">平成28年5月5日</span><span class="title">端午祭・流鏑馬神事</span></li>
      <li><span class="date">平成28年6月30日</span><span class="title">夏越大祓式</span></li>
      <li><span class="date">平成28年7月7日</span><span class="title">七夕祭</span></li>
    </ul>
    <span class="sched-btn">行事予定一覧表</span>
    <div class="banners">
      <div class="banner" role="img" aria-label="湖と鳥居の写真"><span>御船祭</span></div>
      <div class="banner" role="img" aria-label="社殿の写真"><span>御祈祷</span></div>
      <div class="banner" role="img" aria-label="森の参道の写真"><span>奥参道</span></div>
      <div class="banner" role="img" aria-label="鳥居の写真"><span>交通案内</span></div>
    </div>
  </aside>
</div>

<footer class="footer">
  <span class="pagetop">ページの先頭へ</span>
  <div class="f-brand">
    <div class="name"><span class="mark"></span>杜乃宮</div>
    <p>〒000-0000　北原郷森ノ町1-2-3<br>TEL 000-000-0000　FAX 000-000-0001<br>受付時間 8:30〜16:30</p>
  </div>
  <div class="f-map">
    <div>
      <h4>サイトマップ</h4>
      <div class="two">
        <ul><li>杜乃宮について</li><li>御祭神</li><li>由緒・歴史</li><li>祭典・行事</li><li>年間行事</li><li>参拝案内</li></ul>
        <ul><li>ご祈祷</li><li>境内案内</li><li>周辺案内</li><li>御守・御札</li><li>特集</li><li>お問合せ</li></ul>
      </div>
    </div>
    <div><h4>Guide</h4><ul><li>交通案内</li><li>駐車場</li><li>宝物館</li><li>よくある質問</li></ul></div>
    <div><h4>About</h4><ul><li>プライバシー</li><li>サイトについて</li><li>リンク</li><li>English</li></ul></div>
  </div>
</footer>
<div class="copy">Copyright © Morino Miya. All Rights Reserved.</div>

</body>
</html>
```